Etiketten-Design für Honiggläser
Zielgruppe
kleine Hobby-Imkerei, Zielgruppe 'Regionale Käufer', die gerne Wissen, wo ihr Honig her kommt. Mittleres Preissegment
Aufgabenstellung
Das Etikett soll für meine Honiggläser dienen. Die Maße sind 134 x 64 mm. Die Breite kann bis 150 mm variieren, die Höhe nicht.
Pflichtangaben : 'Deutscher xxx Honig (z.B. Blütenhonig), Name und Anschrift (Matthias Kolbe Birkenweg 12 71523 Ludwigsburg M.Kolbe@postfeld.de), mindestens haltbar bis(wird gestempelt, Fläche min. 30x7mm, Gewicht 500 g(Schriftgröße min. 4 mm), 'Mehrwegglas'. Schriftgröße mindestens 1,2mm bezogen auf das kleine „x“. Optional Lagerbedingungen, s. bisheriges Etikett.
Das angehängte Bild soll in irgendeiner Form mit eingebunden wäre, gerne können Farben und Form aber verändert werden, Bildrechte sind bei mir. Anbei auch mein bisheriges, selber entworfenes Etikett.
Das neue Etikett soll moderner und ansprechender werden, der Regionalitätsbezug etwas besser herausgearbeitet werden. Gelb hat sich als Farbe nicht bewährt, da das gelb des Honig sich manchmal beißt.

```html
<!DOCTYPE html>
<html lang="de">
<head>
<meta charset="utf-8">
<title>Honigetikett – Deutscher Honig aus Ludwigsburg</title>
<link href="https://fonts.googleapis.com/css2?family=Maven+Pro:wght@400;500;700&display=swap" rel="stylesheet">
<style>
  :root {
    --page-bg: #fafafa;
    --page-edge: #9a9a9a;
    --label-edge: #222222;
    --ink: #111111;
    --leaf-green: #99cc00;
    --rule: #333333;
    --white: #ffffff;
    --grass-top: #5ea64a;
    --field-yellow: #d8c43a;
    --grass-mid: #3ea72f;
    --grass-low: #2d9427;
  }
  html, body {
    margin: 0;
    padding: 0;
    overflow: hidden;
  }
  body {
    width: 1200px;
    height: 1200px;
    background: var(--page-bg);
    font-family: "Maven Pro", Arial, sans-serif;
    color: var(--ink);
    position: relative;
    box-sizing: border-box;
    border: 1px solid var(--page-edge);
  }
  .label {
    position: absolute;
    left: 187px;
    top: 413px;
    width: 845px;
    height: 404px;
    border: 1px solid var(--label-edge);
    box-sizing: border-box;
    background: var(--white);
    overflow: hidden;
  }
  .front {
    position: absolute;
    left: 0;
    top: 0;
    width: 555px;
    height: 404px;
  }
  .front svg {
    position: absolute;
    left: 0;
    top: 0;
  }
  .front-title {
    position: absolute;
    left: 0;
    width: 555px;
    text-align: center;
    margin: 0;
    font-weight: 500;
    line-height: 1;
  }
  .front-title.main { top: 311px; font-size: 40px; letter-spacing: -0.5px; }
  .front-title.sub { top: 349px; font-size: 24px; font-weight: 400; }

  .info {
    position: absolute;
    left: 555px;
    top: 0;
    width: 290px;
    height: 404px;
  }
  .info > * {
    position: absolute;
    margin: 0;
    line-height: 1;
  }
  .info .centered { left: 0; width: 290px; text-align: center; }
  .info .left { left: 17px; }
  .info .right { right: 15px; text-align: right; }
  .kind-title { top: 28px; font-size: 22px; font-weight: 700; letter-spacing: 0.3px; }
  .kind-sub { top: 56px; font-size: 22px; font-weight: 400; }
  .rule {
    left: 17px;
    width: 257px;
    height: 0;
    border-top: 1px solid var(--rule);
  }
  .address { top: 114px; font-size: 14px; line-height: 18.5px; letter-spacing: 0.2px; }
  .storage { top: 194px; font-size: 14px; }
  .storage-note { top: 215px; font-size: 11px; line-height: 13.5px; width: 260px; }
  .best-before { top: 284px; font-size: 14px; letter-spacing: 0.3px; }
  .weight { top: 341px; font-size: 24px; font-weight: 500; }
  .returnable { top: 375px; font-size: 9px; letter-spacing: 0.4px; }
</style>
</head>
<body>
  <section class="label">
    <div class="front">
      <svg width="555" height="404" viewBox="0 0 555 404">
        <defs>
          <linearGradient id="orchard-tones" x1="0" y1="0" x2="0" y2="1">
            <stop offset="0" stop-color="var(--grass-top)"/>
            <stop offset="0.3" stop-color="var(--field-yellow)"/>
            <stop offset="0.5" stop-color="var(--grass-mid)"/>
            <stop offset="1" stop-color="var(--grass-low)"/>
          </linearGradient>
        </defs>
        <rect class="leaf-field" x="0" y="0" width="555" height="404" fill="var(--leaf-green)"/>
        <path class="white-swoosh" d="M0 226 Q280 300 555 236 L555 0 L0 0 Z" fill="var(--white)"/>
        <path class="orchard-painting" role="img"
              aria-label="Gemälde: blühende Obstbäume über einer Wiese mit vier weißen Bienenstöcken"
              d="M0 218 Q280 292 555 228 L555 0 L0 0 Z" fill="url(#orchard-tones)"/>
      </svg>
      <h1 class="front-title main">Deutscher Honig</h1>
      <p class="front-title sub">aus Ludwigsburg</p>
    </div>

    <div class="info">
      <h2 class="kind-title centered">DEUTSCHER HONIG</h2>
      <p class="kind-sub centered">aus eigener Imkerei</p>
      <div class="rule" style="top:101px"></div>
      <p class="address centered">Matthias Kolbe,<br>Birkenweg 12, 71523 Ludwigsburg,<br>M.Kolbe@postfeld.de</p>
      <div class="rule" style="top:182px"></div>
      <p class="storage left">Trocken, kühl und dunkel lagern</p>
      <p class="storage-note left">Honig kann fest werden, Sie können kristallisierten Honig im Wassebad (bis 40°) wieder verflüssigen</p>
      <p class="best-before left">mind. haltbar bis:</p>
      <div class="rule" style="top:323px"></div>
      <p class="weight right">500g ℮</p>
      <p class="returnable right">MEHRWEGGLAS</p>
    </div>
  </section>
</body>
</html>
```